Crew Novara Product Brochure

This brochure will be an entire overall and in depth tri-fold brochure for our main web application called BrightQuorra and the 8 main modules that can be purchased. We are a 20 year company that is the leading provider in the healthcare industry and have just rebranded our logo, slogan and theme and this must be the same wow factor, corporate, professional, cutting edge design also.

This brochure must be an major upgrade to our current brochure, we have now named our web application to BrightQuorra and it has modules all with the Bright name before it.  To help we have uploaded a document (zip file) with our old brochure, new logo, and content document, and Bright logo. 

All our logos, content, and overall help to the brochures are posted at this link www.crewnovara.example/files/NVR_Info.zip

```html
<!DOCTYPE html>
<html lang="en">
<head>
<meta charset="utf-8">
<title>Crew Novara – BrightQuorra Modules Brochure</title>
<link href="https://fonts.googleapis.com/css2?family=Arimo:wght@400;700&display=swap" rel="stylesheet">
<style>
  :root{
    --navy:#14276b;
    --red:#c8242b;
    --deep:#1c4fae;
    --mid:#2f6fd0;
    --sky:#4d93e6;
    --pale:#dfe9f7;
    --white:#ffffff;
    --ink:#0f1a3a;
    --grey:#8496bb;
  }
  *{margin:0;padding:0;box-sizing:border-box}
  html,body{width:1200px;height:566px;overflow:hidden;background:#fff}
  body{font-family:"Arimo",Arial,sans-serif}
  .spread{position:relative;width:1200px;height:566px;overflow:hidden}
  .panel{position:absolute;top:0;height:566px;width:400px;overflow:hidden}
  .panel--left{left:0;background:linear-gradient(180deg,#2a66c9,#1d4fb0)}
  .panel--middle{left:400px;background:linear-gradient(160deg,#7fb0ec 0%,#5c93dc 50%,#8cbcf0 100%)}
  .panel--right{left:800px;background:linear-gradient(160deg,#e9f0f9 0%,#c9dbf2 60%,#eef3fa 100%)}
  .photo{position:absolute;z-index:1}
  .box{position:absolute;z-index:2;color:var(--white);font-size:11.5px;line-height:16px;hyphens:auto;-webkit-hyphens:auto}
  .box ul{list-style:none}
  .module-title{font-weight:700;font-size:17px;color:var(--navy);line-height:20px;margin-bottom:6px}
  .box--white{background:var(--white);color:var(--ink);z-index:3}
  .box--bold li{font-weight:700}
  .box--tight{line-height:15.5px}
</style>
</head>
<body>
<div class="spread">

  <section class="panel panel--left">
    <div class="photo" role="img" aria-label="Stethoscope on a blue background" style="left:0;top:0;width:130px;height:170px;background:linear-gradient(135deg,#9cc3f2,#3d74cf)"></div>
    <div class="box" style="left:125px;top:0;width:275px;height:192px;background:rgba(28,70,170,.92);padding:10px 0 0 6px">
      <ul>
        <li>&gt;Data Driven Dashboard Intelligence</li>
        <li>&nbsp;&gt;Corporate/Divisional/Regional Rollup Reporting</li>
        <li>&gt;Seamless Integration to Company Intranet</li>
        <li>&gt;Proactive Risk Identification</li>
        <li>&gt;Online Help Desk Support &amp; Chat</li>
        <li>&gt;Award Winning Customer Support</li>
        <li>&gt;Customer Driven, Customized to Meet Your Needs</li>
        <li>&gt;Proven Return on Investment (ROI)</li>
      </ul>
    </div>
    <div class="photo" role="img" aria-label="Medical scan figure with heartbeat line" style="left:215px;top:195px;width:185px;height:150px;background:linear-gradient(135deg,#bcd6f3,#5c8fd6 60%,#2f5fb8)"></div>
    <div class="photo" role="img" aria-label="Modern glass office building" style="left:0;top:395px;width:400px;height:171px;background:linear-gradient(180deg,#8fb2e2,#4e7fcb 55%,#2d5eb4)"></div>
    <div class="box box--white" style="left:25px;top:170px;width:190px;height:225px;padding:26px 4px 0 6px">
      <div class="module-title" style="margin-left:20px">BrightCheck</div>
      <ul>
        <li>&gt;Pre &amp; Post Submission Analysis</li>
        <li>&gt;3,000+ Consistency, Logic, Validation Checks</li>
        <li>&gt;Seamless Integration with MDS Software Vendors</li>
        <li>&gt;Customer Created Accuracy Checks</li>
        <li>&gt;Instant Online Coding Assistance</li>
      </ul>
    </div>
    <div class="box" style="left:105px;top:345px;width:295px;height:120px;background:rgba(77,147,230,.85);padding:28px 0 0 120px">
      <div class="module-title" style="margin-left:28px">BrightRug</div>
      <ul>
        <li>&gt;RUG IV Ready</li>
        <li>&gt;Automated Optimization</li>
        <li>&gt;Opportunity Driven</li>
        <li>&gt;Proven Accuracy</li>
      </ul>
    </div>
  </section>

  <section class="panel panel--middle">
    <div class="photo" role="img" aria-label="Blood sample test tubes in a rack" style="left:240px;top:125px;width:160px;height:175px;background:linear-gradient(160deg,#e8eef6,#b9c9de 60%,#c98b8b)"></div>
    <div class="box" style="left:190px;top:0;width:210px;height:125px;background:rgba(120,176,238,.97);padding:6px 0 0 6px;line-height:15.5px;z-index:3">
      <div class="module-title" style="margin-left:36px;margin-bottom:1px">BrightLearn</div>
      <ul style="color:var(--ink)">
        <li>&gt;Self-paced LTC eLearning online videos</li>
        <li>&gt;On-going monthly webinars</li>
        <li>&gt;Includes industry hot topic tools/resources</li>
        <li>&gt;CEU Approved</li>
      </ul>
    </div>
    <div class="box" style="left:68px;top:78px;width:172px;height:222px;background:rgba(132,150,187,.95);padding:20px 3px 0 6px;line-height:15.5px">
      <div class="module-title" style="margin-left:18px;margin-bottom:6px">BrightPro</div>
      <ul style="color:var(--ink)">
        <li>&gt;Clinical Risk Reporting</li>
        <li>&gt;Real-Time QM/QI Trend &amp; Analysis</li>
        <li>&gt;Functional Decline/Improvement Analysis</li>
        <li>&gt;Sentinel Event Reporting</li>
        <li>&gt;"At Risk" Resident Risk Focus Analysis</li>
        <li>&gt;Clinical/Quality Trend Analysis</li>
        <li>g. Pharmacy Data Integration</li>
      </ul>
    </div>
    <div class="box" style="left:160px;top:300px;width:235px;height:258px;background:rgba(47,111,208,.95);padding:6px 4px 0 6px">
      <div class="module-title" style="margin-left:54px;margin-bottom:2px">BrightReg</div>
      <ul>
        <li>&gt;Federal &amp; State Nursing Home Regulations</li>
        <li>&gt;Includes S &amp; C Letters, Transmittals, MLN Matters, etc.</li>
        <li>&gt;Entire MDS 3.0 RAI Manual</li>
        <li>&gt;QIS Survey Manual</li>
        <li>&gt;OSHA Regs</li>
        <li>&gt;Medicare/Medicaid Publications</li>
        <li>&gt;More than 90,000 pages of regulatory &amp; compliance resources</li>
        <li>&gt;Manage DPNA &amp; Termination Timelines</li>
        <li>&gt;Manage Survey Remedies</li>
        <li>&gt;Manage 2567 Surveyor Notes</li>
        <li>&gt;Includes Trend Reporting/Analysis</li>
      </ul>
    </div>
  </section>

  <section class="panel panel--right">
    <div class="box box--bold" style="left:25px;top:70px;width:225px;height:156px;background:rgba(77,147,230,.9);padding:8px 4px 0 6px">
      <div class="module-title" style="margin-left:36px;margin-bottom:0">BrightQIS</div>
      <ul style="color:var(--ink)">
        <li>&gt;QIS Survey Preparation Tool</li>
        <li>&gt;Incident &amp; Event Management</li>
        <li>&gt;Concern/Grievance Management</li>
        <li>&gt;Quality Improvement/Assurance</li>
        <li>&gt;QA&amp;A Meeting Automation</li>
      </ul>
    </div>
    <div class="box box--bold" style="left:25px;top:228px;width:178px;height:330px;background:rgba(28,79,174,.95);padding:4px 3px 0 4px;font-size:11px;line-height:15px">
      <div class="module-title" style="margin-left:32px;margin-bottom:0">BrightRisk</div>
      <ul>
        <li>&gt;Clinical Risk Trending</li>
        <li>&gt;Survey Performance Risk Trending</li>
        <li>&gt;RUG's Improvement Trending</li>
        <li>&gt;Narrative Risk Reporting</li>
        <li>&gt;Special Focus "At Risk" Reduction Analysis</li>
        <li>&gt;Five Star Staffing/CMI Trending</li>
        <li>&gt;Cross-integrates MDS to Physician Ordered Medications</li>
        <li>&gt;Trends Risk Impact of MDS to Med Data</li>
        <li>&gt;Risk Impact to "At Risk" Residents</li>
        <li>&gt;Identify "At Risk" Survey Tags/Trends</li>
        <li>k. Identify Med-to-MDS Highlights</li>
      </ul>
    </div>
    <div class="box box--white box--bold" style="left:212px;top:170px;width:188px;height:250px;padding:8px 3px 0 4px">
      <div class="module-title" style="margin-left:36px;margin-bottom:2px">BrightTrend</div>
      <ul>
        <li>&gt;Survey Trend &amp; Impact Analysis</li>
        <li>&gt;Pin Point Prediction Analysis</li>
        <li>&gt;Special Focus Facility "At Risk" Analysis</li>
        <li>&gt;Five Star Rating Improvement Analysis</li>
        <li>&gt;Peer Group Comparative Analysis</li>
        <li>&gt;Manage Real-time Survey Results</li>
        <li>&gt;Manage DPNA &amp; Termination Timelines</li>
      </ul>
    </div>
    <div class="photo" role="img" aria-label="Caregiver with a young patient" style="left:212px;top:420px;width:188px;height:146px;background:linear-gradient(135deg,#f3e4de,#d9a9b4 50%,#a8c3e6)"></div>
  </section>

</div>
</body>
</html>
```